Masculine, visually appealing sales presentation for CPA firm

I have a basic power point that I use for sales presentations and I would like it to be updated to be more appealing and modern.

This is a presentation I give to real estate agents to help them close sales, save taxes, and resolve tax disputes. I would like the powerpoint to be updated to be more visually appealing. I have included the current powerpoint along with some of my logo files.

You don't have to use any of the pictures/clip art that is in the current power point. I only care that the words of the powerpoint make it to the new version.

Target Market(s)

Realtors, Real Estate Agents

Industry/Entity Type

Accounting

Requirements
Must have
• Visually appealing. I don't want it to look like I just took a template and made a normal powerpoint out of it. It should look custom.
Should not have
• Anything unprofessional, anything inconsistent with my brand

```html
<!DOCTYPE html>
<html lang="en">
<head>
<meta charset="utf-8">
<title>Home Office</title>
<link rel="stylesheet" href="https://fonts.googleapis.com/css2?family=Carlito:wght@400;700&family=Oswald:wght@700&display=swap">
<style>
  :root {
    --navy: #1c2a3d;
    --navy-deep: #131e2c;
    --sky-top: #eef2f6;
    --sky-low: #c9d4df;
    --ink: #0d0d0d;
    --white: #ffffff;
    --glow: rgba(190, 220, 255, 0.85);
    --scene-a: rgba(120, 140, 160, 0);
    --scene-b: #7d8fa2;
    --scene-c: #2c3a4d;
  }
  * { margin: 0; padding: 0; box-sizing: border-box; }
  html, body { width: 1200px; height: 900px; overflow: hidden; }
  body { background: var(--white); }
  .slide {
    position: relative;
    width: 1200px;
    height: 900px;
    overflow: hidden;
    background: linear-gradient(180deg, var(--sky-top) 0%, #dde4ec 55%, var(--sky-low) 100%);
    font-family: "Carlito", "Calibri", sans-serif;
    color: var(--ink);
  }
  .top-strip {
    position: absolute; left: 0; top: 0; width: 1200px; height: 50px;
    background: linear-gradient(180deg, #f4f6f9, #dfe5ec);
  }
  .header-band {
    position: absolute; left: 0; top: 50px; width: 1200px; height: 164px;
    background: linear-gradient(180deg, var(--navy) 0%, var(--navy-deep) 100%);
  }
  .title {
    position: absolute; right: 98px; top: 70px;
    font-family: "Oswald", "Impact", sans-serif;
    font-weight: 700;
    font-size: 104px;
    line-height: 1;
    letter-spacing: 6px;
    word-spacing: 24px;
    color: var(--white);
    text-shadow: 0 0 10px var(--glow), 0 0 22px rgba(160, 200, 255, 0.5);
  }
  .house-art {
    position: absolute; left: 0; top: 0; width: 300px; height: 230px;
  }
  .workspace-scene {
    position: absolute; left: 560px; top: 214px; width: 640px; height: 668px;
    background:
      radial-gradient(ellipse at 80% 30%, var(--scene-c) 0%, rgba(44,58,77,0.6) 30%, rgba(44,58,77,0) 60%),
      linear-gradient(90deg, var(--scene-a) 0%, rgba(150,165,180,0.35) 30%, var(--scene-b) 100%);
  }
  .points { position: absolute; left: 44px; top: 270px; list-style: none; }
  .point {
    position: relative; padding-left: 30px;
    font-size: 36px; line-height: 1.18; margin-bottom: 14px;
  }
  .point::before {
    content: ""; position: absolute; left: 0; top: 15px;
    width: 9px; height: 9px; border-radius: 50%; background: var(--ink);
  }
  .point b { font-weight: 700; }
  .sub-points { list-style: none; margin-top: 8px; margin-left: 32px; }
  .sub-point {
    position: relative; padding-left: 28px;
    font-size: 31px; line-height: 47px;
  }
  .sub-point::before {
    content: ""; position: absolute; left: 0; top: 20px;
    width: 8px; height: 8px; border-radius: 50%; background: var(--ink);
  }
  .aside-points { list-style: none; margin-left: 28px; }
  .aside-point {
    position: relative; padding-left: 26px;
    font-size: 23px; line-height: 34px;
  }
  .aside-point::before {
    content: ""; position: absolute; left: 0; top: 14px;
    width: 7px; height: 7px; border-radius: 50%; background: var(--ink);
  }
  .mascot-mark {
    position: absolute; left: 38px; top: 790px; width: 76px; height: 76px;
    border-radius: 50%; background: var(--navy);
  }
  .footer-rule {
    position: absolute; left: 650px; top: 834px; width: 538px; height: 2px;
    background: var(--navy-deep);
  }
  .firm-name {
    position: absolute; right: 20px; top: 844px;
    font-weight: 700; font-size: 20px; color: var(--navy-deep);
  }
  .footer-band {
    position: absolute; left: 0; top: 880px; width: 1200px; height: 20px;
    background: var(--navy);
  }
</style>
</head>
<body>
<main class="slide">
  <div class="top-strip"></div>
  <div class="header-band"></div>
  <div class="workspace-scene" role="img" aria-label="Home office desk with computer monitor, keyboard and coffee mug"></div>

  <svg class="house-art" viewBox="0 0 300 230" role="img" aria-label="Illustration of a modern house with pool and a set of keys">
    <defs>
      <linearGradient id="houseTone" x1="0" y1="0" x2="1" y2="1">
        <stop offset="0" stop-color="#f4f6f8"/>
        <stop offset="1" stop-color="#c7cdd3"/>
      </linearGradient>
    </defs>
    <path d="M0 100 L150 40 L300 115 L290 190 L70 230 L0 200 Z" fill="url(#houseTone)"/>
  </svg>

  <h1 class="title">HOME OFFICE</h1>

  <ul class="points">
    <li class="point"><b>Regular and exclusive use</b></li>
    <li class="point"><b>Indirect expenses</b> – must allocate, generally on<br>square footage
      <ul class="sub-points">
        <li class="sub-point">Mortgage interest &amp; property taxes</li>
        <li class="sub-point">Homeowner’s insurance</li>
        <li class="sub-point">Repairs &amp; maintenance</li>
        <li class="sub-point">Rent or depreciation (no land, 39 yrs.)</li>
        <li class="sub-point">Utilities (may require different allocation %)</li>
        <li class="sub-point">Water, sewer, trash, snow plowing, etc.</li>
        <li class="sub-point">Lawn care/landscaping???
          <ul class="aside-points">
            <li class="aside-point">How aggressive are you?!?!</li>
          </ul>
        </li>
      </ul>
    </li>
  </ul>

  <div class="mascot-mark" role="img" aria-label="Firm mark"></div>
  <div class="footer-rule"></div>
  <p class="firm-name">National Guild of Tax Resolution Advisors©</p>
  <div class="footer-band"></div>
</main>
</body>
</html>
```